New Business card design to reflect rebrand

I would like a business card design with a good base colour for our new logo and also a placeholder for a profile pic of the card holder. the design needs to be editable to the point that we can easily change the picture of the person and use that design for printlarkly etc. we are looking at a metalic finish business card so will need a good base colour to bring out the finish.

Target Market(s)

prospective customers

Industry/Entity Type

Business

Contact Information for Business Card

I would like one editable design that we can change the name of the card holder and profile picture. The design need to be in a format that be send to printlarkly etc.

Our address is Fenwick Lodge, Mill Lane, Hartley Wintney, KT14 3WB Tel no. 01632 960418

Requirements
Must have
• place holder for a profile pic for the card holder. in AI or preferably PSD format

```html
<!DOCTYPE html>
<html lang="en">
<head>
<meta charset="utf-8">
<title>Corvane Workplace Services – Business Card</title>
<link href="https://fonts.googleapis.com/css2?family=Lato:wght@400;700&display=swap" rel="stylesheet">
<style>
  :root {
    --navy: #3f5270;
    --orange: #e8620b;
    --white: #ffffff;
    --page: #eceef1;
    --photo-top: #c9c4bd;
    --photo-bottom: #2a2c31;
  }
  * { box-sizing: border-box; margin: 0; padding: 0; }
  html, body { width: 1200px; height: 1200px; overflow: hidden; }
  body {
    background: var(--page);
    font-family: "Lato", Arial, sans-serif;
    display: flex;
    flex-direction: column;
    align-items: center;
    justify-content: center;
    gap: 60px;
  }
  .card {
    position: relative;
    width: 840px;
    height: 480px;
    background: var(--white);
    overflow: hidden;
    box-shadow: 0 6px 20px rgba(0,0,0,.12);
  }

  /* Brand name block */
  .brand {
    display: flex;
    align-items: center;
    gap: 18px;
  }
  .brand-square {
    width: 46px; height: 46px;
    background: var(--orange);
    flex: none;
  }
  .brand-name {
    color: var(--navy);
    font-weight: 700;
    text-transform: uppercase;
    line-height: 1.05;
  }
  .brand-name span { display: block; }
  .brand-name .primary { font-size: 64px; letter-spacing: 2px; }
  .brand-name .secondary { font-size: 23px; letter-spacing: 7px; }

  /* Back */
  .card-back .band-top {
    position: absolute; left: 0; top: 0; width: 100%; height: 102px;
    background: var(--navy);
  }
  .card-back .band-bottom {
    position: absolute; left: 0; bottom: 0; width: 100%; height: 100px;
    background: var(--orange);
    display: flex; align-items: center; justify-content: center;
  }
  .card-back .web {
    color: var(--white); font-weight: 700; font-size: 24px; letter-spacing: 6px;
  }
  .card-back .brand {
    position: absolute; left: 0; right: 0; top: 102px; height: 278px;
    justify-content: center;
  }

  /* Front */
  .card-front .brand { position: absolute; left: 90px; top: 50px; }
  .card-front .brand-name .primary { font-size: 54px; }
  .card-front .brand-name .secondary { font-size: 20px; letter-spacing: 6px; }
  .card-front .band-name {
    position: absolute; left: 0; top: 234px; width: 100%; height: 62px;
    background: var(--navy);
    display: flex; align-items: center; gap: 22px;
    padding-left: 28px;
  }
  .holder-name { color: var(--white); font-size: 27px; text-transform: uppercase; }
  .job-title { color: var(--orange); font-size: 19px; text-transform: uppercase; }
  .card-front .band-contact {
    position: absolute; left: 0; top: 296px; width: 100%; height: 184px;
    background: var(--orange);
  }
  .contact-list {
    position: absolute; left: 28px; top: 24px;
    display: grid;
    grid-template-columns: 232px 260px;
    row-gap: 22px;
    color: var(--white);
    font-size: 19px;
  }
  .contact-item { display: flex; align-items: center; gap: 14px; white-space: nowrap; }
  .contact-item.address { grid-column: 1 / span 2; font-size: 15px; }
  .icon {
    width: 26px; height: 26px; border-radius: 5px;
    background: var(--navy);
    display: flex; align-items: center; justify-content: center; flex: none;
  }
  .icon svg { width: 16px; height: 16px; }
  .photo-placeholder {
    position: absolute; right: 20px; bottom: 0;
    width: 330px; height: 400px;
    background: linear-gradient(180deg, var(--photo-top) 0%, var(--photo-bottom) 70%);
    border-radius: 150px 150px 0 0;
  }
</style>
</head>
<body>

  <!-- Back of card -->
  <section class="card card-back">
    <div class="band-top"></div>
    <div class="brand">
      <div class="brand-square"></div>
      <div class="brand-name">
        <span class="primary">Corvane</span>
        <span class="secondary">Workplace Services</span>
      </div>
    </div>
    <div class="band-bottom"><span class="web">www.website.com</span></div>
  </section>

  <!-- Front of card -->
  <section class="card card-front">
    <div class="brand">
      <div class="brand-square"></div>
      <div class="brand-name">
        <span class="primary">Corvane</span>
        <span class="secondary">Workplace Services</span>
      </div>
    </div>
    <div class="band-name">
      <span class="holder-name">Card Holder Name</span>
      <span class="job-title">Job Title</span>
    </div>
    <div class="band-contact">
      <div class="contact-list">
        <div class="contact-item">
          <span class="icon"><svg viewBox="0 0 16 16"><rect x="4.5" y="1.5" width="7" height="13" rx="1.5" fill="none" stroke="#fff" stroke-width="1.4"/><circle cx="8" cy="12" r=".9" fill="#fff"/></svg></span>
          + 000 - 000 - 000
        </div>
        <div class="contact-item">
          <span class="icon"><svg viewBox="0 0 16 16"><rect x="2" y="4" width="12" height="8.5" rx="1" fill="none" stroke="#fff" stroke-width="1.4"/><path d="M2.5 4.5 8 9l5.5-4.5" fill="none" stroke="#fff" stroke-width="1.4"/></svg></span>
          mail@website.com
        </div>
        <div class="contact-item">
          <span class="icon"><svg viewBox="0 0 16 16"><path d="M4 2h2.5l1 3-1.5 1a7 7 0 0 0 4 4l1-1.5 3 1V12a2 2 0 0 1-2 2A10 10 0 0 1 2 4a2 2 0 0 1 2-2z" fill="#fff"/></svg></span>
          + 000 - 000 - 000
        </div>
        <div class="contact-item">
          <span class="icon"><svg viewBox="0 0 16 16" fill="none" stroke="#fff" stroke-width="1.2"><circle cx="8" cy="8" r="6"/><ellipse cx="8" cy="8" rx="2.6" ry="6"/><path d="M2 8h12M3 5h10M3 11h10"/></svg></span>
          www.website.com
        </div>
        <div class="contact-item address">
          <span class="icon"><svg viewBox="0 0 16 16"><path d="M8 1.5a4.5 4.5 0 0 0-4.5 4.5C3.5 9.5 8 14.5 8 14.5s4.5-5 4.5-8.5A4.5 4.5 0 0 0 8 1.5z" fill="#fff"/><circle cx="8" cy="6" r="1.6" fill="#3f5270"/></svg></span>
          Address: Street No, Nord Avenue, Co,City/State Zipcode
        </div>
      </div>
    </div>
    <div class="photo-placeholder" role="img" aria-label="Profile photo of the card holder in a dark suit, arms crossed"></div>
  </section>

</body>
</html>
```